I am a coffee roaster. We import and sell some of the finest coffee you can buy.

I am needing a package design for coffee. Our coffee is some of the finest you can buy so I am wanting a packaging that shows that. I have our brand logo but really need the packaging created.

Estate Grown Arabica coffees from countries make up Borvath Select blends. Only a handful of the world’s premiere coffee beans can produce the flavor, richness, and aroma that make Borvath Select coffees stand out from traditionally grown coffees. Ingredients: Coffee Tamsick-Orvell Beverage 800-316-2758 www.tobeverage.example

```html
<!DOCTYPE html>
<html lang="en">
<head>
<meta charset="utf-8">
<title>Borvath Select – Fresh Premium Coffee Pouch</title>
<link rel="stylesheet" href="https://fonts.googleapis.com/css2?family=Josefin+Sans:wght@300;400;600&display=swap">
<style>
  :root {
    --backdrop: #ececec;
    --pouch-black: #1e1e20;
    --pouch-black-soft: #2a2a2d;
    --brand-red: #8e1b24;
    --label-white: #ffffff;
    --brand-bronze: #8a5a2b;
    --title-cream: #ece6dc;
    --rule-gold: #b0873f;
    --bean-dark: #2b160d;
    --bean-mid: #5a2e17;
    --bean-light: #7a4222;
    --fine-print: #6d6d70;
  }
  * { box-sizing: border-box; margin: 0; padding: 0; }
  html, body {
    width: 1200px;
    height: 1000px;
    overflow: hidden;
    background: var(--backdrop);
    font-family: "Josefin Sans", sans-serif;
  }
  .canvas {
    position: relative;
    width: 1200px;
    height: 1000px;
  }
  .pouch {
    position: absolute;
    left: 390px;
    top: 140px;
    width: 420px;
    height: 720px;
    background: linear-gradient(180deg, var(--pouch-black-soft) 0%, var(--pouch-black) 40%);
    border-radius: 10px 10px 4px 4px;
    overflow: hidden;
  }
  .pouch__seal {
    position: absolute;
    left: 0; right: 0; top: 0;
    height: 20px;
    border-bottom: 1px solid rgba(255,255,255,0.06);
  }
  .pouch__zip {
    position: absolute;
    left: 0; right: 0; top: 72px;
    height: 4px;
    border-top: 1px solid rgba(255,255,255,0.08);
    border-bottom: 1px solid rgba(0,0,0,0.35);
  }
  .brand-band {
    position: absolute;
    left: 132px;
    top: 0;
    width: 146px;
    height: 120px;
    background: var(--brand-red);
  }
  .brand-seal {
    position: absolute;
    left: 132px;
    top: 68px;
    width: 146px;
    height: 146px;
    border-radius: 50%;
    background: var(--label-white);
    border: 4px solid var(--brand-red);
    display: flex;
    align-items: center;
    justify-content: center;
    text-align: center;
  }
  .brand-seal__name {
    font-weight: 600;
    font-size: 19px;
    line-height: 1.1;
    letter-spacing: 0.04em;
    color: var(--brand-bronze);
    text-transform: uppercase;
  }
  .product-title {
    position: absolute;
    left: 0; right: 0;
    top: 258px;
    text-align: center;
    font-weight: 300;
    font-size: 30px;
    letter-spacing: 0.01em;
    color: var(--title-cream);
  }
  .product-rule {
    position: absolute;
    left: 90px;
    width: 240px;
    top: 308px;
    height: 1px;
    background: linear-gradient(90deg, transparent, var(--rule-gold), transparent);
  }
  .bean-photo {
    position: absolute;
    left: 16px;
    right: 16px;
    top: 350px;
    height: 315px;
    background:
      radial-gradient(ellipse at 60% 65%, var(--bean-light) 0%, transparent 55%),
      linear-gradient(180deg, var(--bean-dark) 0%, var(--bean-mid) 45%, var(--bean-dark) 100%);
  }
  .fine-print {
    position: absolute;
    left: 40px;
    right: 70px;
    top: 678px;
    font-size: 8px;
    color: var(--fine-print);
    text-align: center;
    white-space: nowrap;
  }
  .blend-name {
    position: absolute;
    left: 0; right: 0;
    top: 700px;
    font-size: 9px;
    color: #4a3a2a;
    text-align: center;
  }
  .weight-badge {
    position: absolute;
    right: 22px;
    top: 668px;
    width: 28px;
    height: 28px;
    border-radius: 50%;
    background: var(--brand-red);
    color: var(--label-white);
    font-size: 11px;
    font-weight: 600;
    display: flex;
    align-items: center;
    justify-content: center;
  }
</style>
</head>
<body>
  <main class="canvas">
    <section class="pouch">
      <div class="pouch__seal"></div>
      <div class="brand-band"></div>
      <div class="pouch__zip"></div>
      <div class="brand-seal">
        <span class="brand-seal__name">Borvath<br>Select</span>
      </div>
      <h1 class="product-title">Fresh Premium Coffee</h1>
      <div class="product-rule"></div>
      <div class="bean-photo" role="img" aria-label="Roasted coffee beans with sketched line drawing of three beans"></div>
      <p class="fine-print">Estate grown arabica beans, slow roasted in small batches for richness</p>
      <p class="blend-name">Arabica Blend</p>
      <div class="weight-badge">1kg</div>
    </section>
  </main>
</body>
</html>
```